Business Card Design - Carrington Hill Lodge

We are looking at a new design for our business cards that has a modern and professional look. We run a residential aged care facility focussing on the care of residents. The cards will be used for potential clients, consultants and business opportunities in this sector. Blue and white is our main colours and would to see these colours incorporated in the design.
Industry/Entity Type
Business
Contact Information for Business Card
Carrington Hill Lodge, Darren Pelham, dpelham@carringtonhilllodge.com.au, Finance Manager, 0491 736 208, BCom, 48 Yarrabee Way, Marlow Park, Qld 4165.

```html
<!DOCTYPE html>
<html lang="en">
<head>
<meta charset="utf-8">
<title>Carrington Hill Lodge – Business Card</title>
<link href="https://fonts.googleapis.com/css2?family=Open+Sans:wght@400;600&display=swap" rel="stylesheet">
<style>
  :root {
    --brand-blue: #4c7a95;
    --band-grey: #aba39d;
    --card-white: #ffffff;
    --backdrop: #e9e6e3;
    --text-font: "Open Sans", Arial, sans-serif;
  }
  * { box-sizing: border-box; margin: 0; padding: 0; }
  html, body {
    width: 1200px; height: 900px; overflow: hidden;
    background: var(--backdrop);
    font-family: var(--text-font);
  }
  .canvas { position: relative; width: 1200px; height: 900px; }

  .card {
    position: absolute;
    box-shadow: 0 6px 18px rgba(0,0,0,.18);
    overflow: hidden;
  }
  .card-front { left: 78px; top: 33px; width: 588px; height: 365px; background: var(--card-white); }
  .card-back { left: 388px; top: 505px; width: 567px; height: 352px; background: var(--brand-blue); }

  .front-shapes { position: absolute; inset: 0; }

  .brand-mark {
    position: absolute; left: 0; width: 100%;
    display: flex; flex-direction: column; align-items: center;
  }
  .card-front .brand-mark { top: 28px; }
  .card-back .brand-mark { top: 92px; }
  .brand-dot { border-radius: 50%; }
  .card-front .brand-dot { width: 96px; height: 96px; background: var(--brand-blue); margin-bottom: 16px; transform: translateX(3px); }
  .card-back .brand-dot { width: 112px; height: 112px; background: var(--card-white); margin-bottom: 20px; }
  .brand-name {
    font-weight: 400; text-transform: uppercase; letter-spacing: 2px; white-space: nowrap;
  }
  .card-front .brand-name { font-size: 21px; color: var(--brand-blue); transform: translateX(4px); }
  .card-back .brand-name { font-size: 24px; color: var(--card-white); }

  .contact-lines {
    position: absolute; right: 282px; top: 270px;
    text-align: right; color: var(--card-white); font-size: 15px; line-height: 25px;
  }
  .contact-line { display: flex; justify-content: flex-end; align-items: center; gap: 5px; white-space: nowrap; }
  .contact-line svg { width: 12px; height: 12px; fill: var(--card-white); flex: none; }

  .person {
    position: absolute; left: 335px; top: 230px; color: var(--card-white);
  }
  .person-name { font-size: 20px; font-weight: 600; line-height: 28px; white-space: nowrap; }
  .person-name .credential { font-size: 15px; }
  .person-role { font-size: 15px; line-height: 22px; }
  .person-address { font-size: 15px; line-height: 24px; margin-top: 17px; white-space: nowrap; }
</style>
</head>
<body>
<main class="canvas">

  <section class="card card-front">
    <svg class="front-shapes" width="588" height="365" viewBox="0 0 588 365">
      <polygon points="0,200 405,200 385,227 0,227" fill="var(--band-grey)"/>
      <polygon points="0,229 392,229 418,192 588,192 588,365 0,365" fill="var(--brand-blue)"/>
    </svg>

    <div class="brand-mark">
      <div class="brand-dot"></div>
      <div class="brand-name">Carrington Hill Lodge</div>
    </div>

    <div class="contact-lines">
      <div class="contact-line">0491 736 208
        <svg viewBox="0 0 24 24"><path d="M6.6 10.8a15.1 15.1 0 0 0 6.6 6.6l2.2-2.2c.3-.3.7-.4 1-.2 1.1.4 2.3.6 3.6.6.6 0 1 .4 1 1V20c0 .6-.4 1-1 1A17 17 0 0 1 3 4c0-.6.4-1 1-1h3.5c.6 0 1 .4 1 1 0 1.3.2 2.5.6 3.6.1.3 0 .7-.2 1z"/></svg>
      </div>
      <div class="contact-line">dpelham@carringtonhilllodge.com.au
        <svg viewBox="0 0 24 24"><path d="M2 5h20v14H2z M3.5 6.5 12 13l8.5-6.5" fill="var(--card-white)" stroke="var(--brand-blue)" stroke-width="1.6"/></svg>
      </div>
    </div>

    <div class="person">
      <div class="person-name">Darren Pelham, <span class="credential">BCom</span></div>
      <div class="person-role">Finance Manager</div>
      <div class="person-address">48 Yarrabee Way,<br>Marlow Park, Qld 4165</div>
    </div>
  </section>

  <section class="card card-back">
    <div class="brand-mark">
      <div class="brand-dot"></div>
      <div class="brand-name">Carrington Hill Lodge</div>
    </div>
  </section>

</main>
</body>
</html>
```